Veltrane New Business Card Design IT Company

PLEASE CHECK ATTACHED PDF DOC FOR DETAILS. I have put exactly what I want to save time and finish the project asap thanks.

Veltrane Consulting is an Information Management Consulting company providing IT Professional Services Consulting services to both Public and private sector.
Need a Business Card Design to represent. It has to be Premium Raised Spot Glass finish.
Company Name: Veltrane Consulting
Company Website: veltrane-example.com.au
Company Slogan: High Performance Meets Excellence
Name on Card: Lor Bemis
Title: Managing Partner
Email: Lor.Bemis@veltrane-example.com.au
Phone: 0400000000

Company Logo is under construction from SketchHive
Company Logo & Company Name Font Color should Match and have to Electric Aqua Blue
Company Logo at the Back Side of the Card
Card Background color preference: Slight Grey or Black to make the logo and company Name stand Out.

Any Questions please Ask.

Industry/Entity Type

Construction

Contact Information for Business Card

PLEASE CHECK ATTACHED PDF DOC FOR DETAILS. I have put exactly what I want to save time and finish the project asap thanks
Name on Card: Lor Bemis
Title: Managing Partner
Phone: 0400000000

Requirements
Must have
• PLEASE CHECK ATTACHED PDF DOC FOR DETAILS. I have put exactly what I want to save time and finish the project asap thanks
• Company Logo, Company Name, Company website Company Slogan at the back side of the Card with custom dark blue front and back background
• Company Logo, Company Name , Company Website at the Front of the Card Title and Name email and phone in the front also in white color font
Should not have
• Should not Have Decorative or Script Fonts
• Its a IT company so must be professional no flowers or waterfalls etc

```html
<!DOCTYPE html>
<html lang="en">
<head>
<meta charset="utf-8">
<title>Veltrane Consulting – Business Card</title>
<link rel="stylesheet" href="https://fonts.googleapis.com/css2?family=Arimo:wght@400;700&family=Orbitron:wght@700&display=swap">
<style>
  :root {
    --page: #e9e7e4;
    --card-dark: #0d0f11;
    --card-mid: #1a1d21;
    --band: #050607;
    --aqua: #5ccbe3;
    --aqua-text: #6fd6ea;
    --ink: #0c1a22;
    --white: #f2f4f5;
    --muted: #cfd6da;
  }
  * { box-sizing: border-box; margin: 0; padding: 0; }
  html, body { width: 875px; height: 1200px; overflow: hidden; background: var(--page); }
  body { position: relative; font-family: "Arimo", Arial, sans-serif; }

  .card {
    position: absolute;
    left: 50px;
    width: 774px;
    height: 453px;
    overflow: hidden;
    background:
      radial-gradient(ellipse at 35% 40%, #23272c 0%, transparent 60%),
      linear-gradient(160deg, var(--card-mid) 0%, var(--card-dark) 70%);
    box-shadow: 0 10px 24px rgba(0,0,0,0.35);
  }
  .card--front { top: 116px; }
  .card--back  { top: 630px; background:
      radial-gradient(ellipse at 60% 55%, #262b31 0%, transparent 65%),
      linear-gradient(160deg, #1c2024 0%, #0e1013 75%); }

  .band {
    position: absolute;
    left: 0;
    top: 47px;
    height: 44px;
    background: var(--band);
  }
  .card--front .band { width: 580px; }
  .card--back .band { top: 51px; width: 100%; }

  .holder {
    position: absolute;
    right: 44px;
    top: 46px;
    text-align: right;
    padding-right: 12px;
    border-right: 3px solid var(--white);
    height: 46px;
  }
  .holder__name {
    font-family: "Orbitron", "Arimo", sans-serif;
    font-weight: 700;
    font-size: 19px;
    letter-spacing: 1px;
    color: var(--aqua-text);
    line-height: 24px;
  }
  .holder__title {
    font-size: 12px;
    color: var(--white);
    letter-spacing: 0.5px;
  }

  .brand {
    position: absolute;
    text-align: center;
  }
  .brand__name {
    font-family: "Arimo", Arial, sans-serif;
    font-weight: 400;
    color: var(--aqua-text);
  }
  .brand__slogan {
    color: var(--white);
    text-transform: uppercase;
    letter-spacing: 0.4px;
  }
  .card--front .brand { left: 60px; top: 190px; width: 250px; }
  .card--front .brand__name { font-size: 24px; }
  .card--front .brand__slogan { font-size: 12px; margin-top: 8px; }
  .card--back .brand { left: 0; right: 0; top: 180px; }
  .card--back .brand__name { font-size: 36px; }
  .card--back .brand__slogan { font-size: 18px; margin-top: 12px; }

  .contact-panel {
    position: absolute;
    left: 349px;
    top: 171px;
    width: 425px;
    height: 126px;
    background: var(--aqua);
    padding: 12px 16px 0 0;
  }
  .contact {
    display: flex;
    justify-content: flex-end;
    align-items: center;
    gap: 14px;
    font-size: 13px;
    color: var(--ink);
    line-height: 17px;
    text-align: right;
  }
  .contact + .contact { margin-top: 10px; }
  .contact svg { width: 14px; height: 14px; flex: none; fill: var(--ink); }

  .ornament-area {
    position: absolute;
    left: 8px;
    top: 132px;
    width: 160px;
    height: 265px;
    background: radial-gradient(ellipse at 45% 50%, rgba(120,130,140,0.22) 0%, rgba(120,130,140,0) 70%);
  }
</style>
</head>
<body>

  <section class="card card--front" aria-label="Business card front">
    <div class="band"></div>
    <div class="holder">
      <div class="holder__name">LOR BEMIS</div>
      <div class="holder__title">MANAGING PARTNER</div>
    </div>

    <div class="brand">
      <div class="brand__name">Veltrane Consulting</div>
      <div class="brand__slogan">High Performance Meets Excellence</div>
    </div>

    <div class="contact-panel">
      <div class="contact">
        <span>12 Floor 100 HARBOUR ROAD<br>Melbourne VIC 3000 AUSTRALIA</span>
        <svg viewBox="0 0 24 24" aria-hidden="true"><path d="M12 2a7 7 0 0 0-7 7c0 5 7 13 7 13s7-8 7-13a7 7 0 0 0-7-7zm0 9.5A2.5 2.5 0 1 1 12 6.5a2.5 2.5 0 0 1 0 5z"/></svg>
      </div>
      <div class="contact">
        <span>0400000000</span>
        <svg viewBox="0 0 24 24" aria-hidden="true"><path d="M3 7c0-2 4-4 9-4s9 2 9 4v2h-5V7H8v2H3zM6 10h12l2 10H4zm6 3a3 3 0 1 0 0 6 3 3 0 0 0 0-6z"/></svg>
      </div>
      <div class="contact">
        <span>Lor.Bemis@veltrane-example.com.au</span>
        <svg viewBox="0 0 24 24" aria-hidden="true"><path d="M12 2l9 5v10l-9 5-9-5V7zm0 5a5 5 0 1 0 0 10 5 5 0 0 0 0-10zm0 3a2 2 0 1 1 0 4 2 2 0 0 1 0-4z"/></svg>
      </div>
    </div>
  </section>

  <section class="card card--back" aria-label="Business card back">
    <div class="band"></div>
    <div class="ornament-area" role="img" aria-label="Faint swirling flourish decoration"></div>
    <div class="brand">
      <div class="brand__name">Veltrane Consulting</div>
      <div class="brand__slogan">High Performance Meets Excellence</div>
    </div>
  </section>

</body>
</html>
```